Business Cards

Business card design for my company.
I would like the card's background colour to be black. You can also see our web site to get an idea of our brand. https://www.tmwhomecrafting.com.au/
- Name
- Email

```html
<!DOCTYPE html>
<html lang="en">
<head>
<meta charset="utf-8">
<title>TMW Home Crafting – Business Cards</title>
<link rel="stylesheet" href="https://fonts.googleapis.com/css2?family=Audiowide&family=Crimson+Pro:wght@500&display=swap">
<style>
  :root {
    --page-bg: #e6e6e6;
    --card-black: #000000;
    --green-bright: #0b9444;
    --green-mid: #068a3c;
    --green-dark: #00702f;
    --white: #ffffff;
  }
  * { margin: 0; padding: 0; box-sizing: border-box; }
  html, body { width: 1200px; height: 849px; overflow: hidden; }
  body { background: var(--page-bg); position: relative; }

  .card {
    position: absolute;
    left: 320px;
    width: 560px;
    height: 320px;
    overflow: hidden;
    background: var(--card-black);
  }
  .card--front { top: 80px; }
  .card--back { top: 449px; }
  .card__art { position: absolute; inset: 0; width: 100%; height: 100%; }

  .brand-name {
    position: absolute;
    font-family: "Audiowide", sans-serif;
    color: var(--white);
    white-space: nowrap;
  }
  .card--front .brand-name {
    left: 228px; top: 150px;
    transform: translateX(-50%);
    font-size: 24px;
    letter-spacing: 0.5px;
  }
  .card--back .brand-name {
    left: 176px; top: 30px;
    font-size: 10px;
  }

  .holder {
    position: absolute;
    left: 348px; top: 20px;
    font-family: "Audiowide", sans-serif;
    color: var(--white);
  }
  .holder__name {
    font-size: 21px;
    line-height: 1.1;
    padding-bottom: 2px;
    border-bottom: 1.5px solid var(--white);
    white-space: nowrap;
  }
  .holder__role { font-size: 11px; margin-top: 3px; }

  .contacts {
    position: absolute;
    right: 25px; top: 98px;
    list-style: none;
  }
  .contacts__item {
    display: flex;
    align-items: center;
    justify-content: flex-end;
    gap: 14px;
    height: 28px;
    margin-bottom: 8px;
    font-family: "Crimson Pro", serif;
    font-weight: 500;
    font-size: 16px;
    color: var(--white);
    white-space: nowrap;
  }
  .contacts__icon { width: 28px; height: 28px; flex: none; }
</style>
</head>
<body>

<section class="card card--front" aria-label="Card front">
  <svg class="card__art" viewBox="0 0 688 394" preserveAspectRatio="none" aria-hidden="true">
    <rect width="688" height="394" fill="var(--green-bright)"/>
    <path d="M560 0 H688 V230 C640 300 560 360 474 394 H470 C560 330 600 160 560 0 Z" fill="var(--green-mid)"/>
    <path d="M472 0 H600 C640 130 600 300 474 394 H472 Z" fill="var(--green-dark)"/>
    <path d="M0 0 H472 C560 110 565 290 472 394 H0 Z" fill="var(--card-black)"/>
  </svg>
  <div class="brand-name">TMW Home Crafting</div>
</section>

<section class="card card--back" aria-label="Card back">
  <svg class="card__art" viewBox="0 0 688 394" preserveAspectRatio="none" aria-hidden="true">
    <rect width="688" height="394" fill="var(--card-black)"/>
    <rect width="260" height="394" fill="var(--green-bright)"/>
    <path d="M0 0 H110 C70 120 130 300 215 394 H0 V300 C60 330 120 360 150 394 Z" fill="var(--green-mid)"/>
    <path d="M110 0 H215 C120 90 120 300 215 394 H170 C60 300 60 110 110 0 Z" fill="var(--green-dark)"/>
    <path d="M215 0 H688 V394 H215 C130 310 120 90 215 0 Z" fill="var(--card-black)"/>
  </svg>

  <div class="brand-name">TMW Home Crafting</div>

  <div class="holder">
    <div class="holder__name">Reid Calloway</div>
    <div class="holder__role">General Manager</div>
  </div>

  <ul class="contacts">
    <li class="contacts__item">
      <span>0400 123 456</span>
      <svg class="contacts__icon" viewBox="0 0 28 28" aria-hidden="true">
        <circle cx="14" cy="14" r="14" fill="var(--white)"/>
        <path d="M10 8 l3 3 -1.5 2 q1.5 3 4 4 l2 -1.5 3 3 -2 2 q-6 0 -10 -7 q-1 -3 2.5 -5.5z" fill="var(--card-black)"/>
      </svg>
    </li>
    <li class="contacts__item">
      <span>info@tmwhomecrafting.com.au</span>
      <svg class="contacts__icon" viewBox="0 0 28 28" aria-hidden="true">
        <circle cx="14" cy="14" r="14" fill="var(--white)"/>
        <rect x="8" y="10" width="12" height="8.5" fill="none" stroke="var(--card-black)" stroke-width="1.3"/>
        <path d="M8 10 L14 15 L20 10" fill="none" stroke="var(--card-black)" stroke-width="1.3"/>
      </svg>
    </li>
    <li class="contacts__item">
      <span>tmwhomecrafting.com.au</span>
      <svg class="contacts__icon" viewBox="0 0 28 28" aria-hidden="true">
        <circle cx="14" cy="14" r="14" fill="var(--white)"/>
        <g fill="none" stroke="var(--card-black)" stroke-width="1">
          <circle cx="14" cy="14" r="6.5"/>
          <ellipse cx="14" cy="14" rx="3" ry="6.5"/>
          <path d="M7.5 14 H20.5 M8.5 10.5 H19.5 M8.5 17.5 H19.5"/>
        </g>
      </svg>
    </li>
    <li class="contacts__item">
      <span>Harbourside, Tasmania, Australia</span>
      <svg class="contacts__icon" viewBox="0 0 28 28" aria-hidden="true">
        <circle cx="14" cy="14" r="14" fill="var(--white)"/>
        <path d="M14 21 C10 16 9 14 9 12 a5 5 0 0 1 10 0 c0 2 -1 4 -5 9z" fill="var(--card-black)"/>
        <circle cx="14" cy="12" r="2" fill="var(--white)"/>
      </svg>
    </li>
  </ul>
</section>

</body>
</html>
```